Poster for a 100 y.o. Tennis Tournament

I would like a poster designed to promote our tennis tournament but I'd like to avoid some of the clichés like the shadow of a player serving. Just well styled text would be fine but some clever imagery would be a bonus.
Highlighting the fact our tournament has been running for over 100 years would be nice so a retro design would work. But that doesn't mean a modern design, for example a minimalist approach utilising the lines of a tennis court, wouldn't work.
Updates

Our tennis committee is now in the process of short listing and will provide an update within 48 hours.

Industry/Entity Type

Court

Requirements
Must have
• The poster must contain the following text at a minimum:
"Marbury Tennis Tournament"/"Since 1908"
"9 March - 11 March, 2013" or "9-11 March, 2013", etc
"www.marburytennis.com.au"

The poster must be reproducible in colour and black & white, or at least have an alternate for black & white.

The poster must be usable in both A3 and A4 sizes.
Nice to have
• The poster should contain the following text:
"Championship"
"Handicap"
"Seniors"
"Juniors"
Each above may be optionally succeeded by "Singles & Doubles", e.g. "Championship Singles & Doubles". It would actually be clearer if this additional text was used but would be repetitive, so alternate text "Singles & Doubles in all categories" might also be used. Alternatives for variety (with the first word the focus): "Championship Singles & Doubles", "Handicap Singles & Doubles", "Seniors 35+ & 50+", "Juniors 18&U, 14&U"

Ideally the poster will provision room for four to eight sponsors logos, preferably at the bottom, but failure to do this is not a show stopper.

The following text may also be used:
"Entries close February 24"
"Tollard Plate Weekend"

Attached is a photo of one of the old trophies. Utilisation of the curved style of the "Marbury Tennis Tournament" text would fit in with the history if the tournament.

The ability to reuse elements of the poster in a single page website used to promote the tournament would be an advantage (as it will provide consistency).

If you could have an image of a tennis ball that conveys the same energy as the clock/tyre image in the attached "Under the Glass Moon" poster, that would be cool. Or using split imagery of a wooden racquet and a modern racquet, but with some energy, would also be good. These are just ideas though and by no means essential.

I've also attached a photo of a t-shirt with a poster layout I thought looked good.

Some additional text that can be used:
"Brand new courts"
"Brindle Park, Oakhurst Tce, Marbury"
"Phone 0427 318 642"
"Prizes and Trophies"

```html
<!DOCTYPE html>
<html lang="en">
<head>
<meta charset="utf-8">
<title>Marbury Tennis Tournament 2013</title>
<link rel="stylesheet" href="https://fonts.googleapis.com/css2?family=Stint+Ultra+Condensed&family=Oswald:wght@300;400&family=Archivo+Narrow:ital,wght@0,400;1,400&family=Libre+Caslon+Text:ital@1&display=swap">
<style>
  :root {
    --paper: #ffffff;
    --ink: #111111;
    --ornament-tone: #6b6b6b;
    --ornament-soft: #bdbdbd;
  }
  * { margin: 0; padding: 0; box-sizing: border-box; }
  html, body { width: 848px; height: 1200px; overflow: hidden; background: var(--paper); }
  .poster {
    position: relative;
    width: 848px;
    height: 1200px;
    overflow: hidden;
    background: var(--paper);
    color: var(--ink);
    text-align: center;
  }
  .frame-border {
    position: absolute;
    left: 43px; top: 43px;
    width: 762px; height: 1111px;
    border: 18px solid var(--ornament-soft);
  }
  .scroll-ornament {
    position: absolute;
    left: 256px;
    width: 336px;
    height: 78px;
    border-radius: 39px;
    background: linear-gradient(90deg, var(--ornament-tone), var(--ornament-soft) 50%, var(--ornament-tone));
  }
  .scroll-ornament--top { top: 6px; }
  .scroll-ornament--bottom { top: 1112px; }
  .line { position: absolute; left: 0; width: 100%; white-space: nowrap; }
  .anniversary {
    top: 148px;
    font-family: "Archivo Narrow", sans-serif;
    font-style: italic;
    font-size: 19px;
    letter-spacing: 0.06em;
  }
  .title {
    font-family: "Stint Ultra Condensed", serif;
    font-size: 120px;
    line-height: 1;
    letter-spacing: 0.02em;
  }
  .title--first { top: 226px; }
  .title--second { top: 364px; }
  .founded {
    top: 562px;
    font-family: "Stint Ultra Condensed", serif;
    font-style: oblique 10deg;
    font-size: 30px;
    letter-spacing: 0.08em;
  }
  .dates {
    top: 618px;
    font-family: "Oswald", sans-serif;
    font-weight: 300;
    font-size: 66px;
    line-height: 1;
  }
  .weekend {
    top: 716px;
    font-family: "Stint Ultra Condensed", serif;
    font-size: 46px;
    line-height: 1;
    letter-spacing: 0.03em;
    transform: scaleY(1.6);
    transform-origin: center top;
  }
  .entries {
    top: 812px;
    font-family: "Archivo Narrow", sans-serif;
    font-size: 29px;
    letter-spacing: 0.02em;
  }
  .categories {
    top: 893px;
    font-family: "Archivo Narrow", sans-serif;
    font-size: 17px;
    line-height: 24px;
  }
  .categories em {
    font-family: "Libre Caslon Text", serif;
    font-size: 16px;
  }
  .website {
    top: 1026px;
    font-family: "Archivo Narrow", sans-serif;
    font-size: 19px;
  }
</style>
</head>
<body>
  <main class="poster">
    <div class="frame-border" role="img" aria-label="Chain of small outlined diamonds forming a decorative border"></div>
    <div class="scroll-ornament scroll-ornament--top" role="img" aria-label="Pair of black curling scroll flourishes"></div>
    <div class="scroll-ornament scroll-ornament--bottom" role="img" aria-label="Pair of black curling scroll flourishes"></div>

    <p class="line anniversary">CELEBRATING 105 YEARS</p>
    <h1>
      <span class="line title title--first">MARBURY TENNIS</span>
      <span class="line title title--second">TOURNAMENT</span>
    </h1>
    <p class="line founded">- SINCE 1908 -</p>
    <p class="line dates">9-11 March 2013</p>
    <p class="line weekend">TOLLARD PLATE WEEKEND</p>
    <p class="line entries">ENTRIES CLOSE FEBRUARY 24</p>
    <p class="line categories">
      &bull; Championship &bull; Handicap &bull; Seniors &bull; Juniors &bull;<br>
      <em>Singles &amp; Doubles in all categories</em><br>
      Seniors 35+ &amp; 50+ &bull; Juniors 18&amp;U, 14&amp;U
    </p>
    <p class="line website">www.marburytennis.com.au</p>
  </main>
</body>
</html>
```